BOLD & MINIMALIST DESIGN NEEDED

We want a very bold but minimalistic business card design that is impactful and utilizes both sides of the business card. Our current logo is included for your use.

We want bold fonts and good use of negative space. We don't want the logo to overpower the design.

Target Market(s)

Professionals who are building new commercial buildings.

Industry/Entity Type

Construction

Contact Information for Business Card

Name, Title, email, office phone, cell phone, website

Font styles to use
Serif
Sans Serif

Requirements
Must have
• Bold design!

```html
<!DOCTYPE html>
<html lang="en">
<head>
<meta charset="utf-8">
<title>Ridgemont Business Card</title>
<link rel="stylesheet" href="https://fonts.googleapis.com/css2?family=Montserrat:wght@400;500;700;800&display=swap">
<style>
  :root {
    --page-bg: #e6e6e6;
    --card-bg: #ffffff;
    --ink: #111111;
    --green-light: #e1efd0;
    --green-mid: #b4dc8a;
    --green-deep: #7fc241;
    --bar: #0d0d0d;
    --icon: #ffffff;
  }
  * { box-sizing: border-box; margin: 0; padding: 0; }
  html, body {
    width: 1200px;
    height: 1200px;
    overflow: hidden;
    background: var(--page-bg);
    font-family: "Montserrat", Arial, sans-serif;
    color: var(--ink);
  }
  .card {
    position: absolute;
    left: 162px;
    width: 876px;
    height: 513px;
    background: var(--card-bg);
  }
  .card--front { top: 71px; }
  .card--back { top: 616px; }

  .contact-panel {
    position: absolute;
    left: 48px;
    top: 0;
    width: 411px;
    height: 443px;
    background: linear-gradient(180deg, var(--green-light) 0%, var(--green-mid) 55%, var(--green-deep) 100%);
  }
  .person {
    position: absolute;
    right: 48px;
    top: 141px;
    text-align: right;
  }
  .person__name {
    font-size: 35px;
    font-weight: 800;
    letter-spacing: 0.2px;
    line-height: 1;
  }
  .person__title {
    font-size: 25px;
    font-weight: 400;
    margin-top: 8px;
    line-height: 1;
  }
  .contact-list {
    position: absolute;
    right: 96px;
    top: 264px;
    list-style: none;
    text-align: right;
  }
  .contact-list li {
    font-size: 21px;
    font-weight: 500;
    height: 40.5px;
    line-height: 32px;
  }
  .icon-bar {
    position: absolute;
    left: 332px;
    top: 240px;
    width: 41px;
    height: 203px;
    background: var(--bar);
    clip-path: polygon(0 12px, 100% 0, 100% 100%, 0 100%);
  }
  .icon-bar svg {
    position: absolute;
    left: 11px;
    width: 19px;
    height: 19px;
    fill: none;
    stroke: var(--icon);
    stroke-width: 2;
  }
  .icon--phone { top: 31px; }
  .icon--mobile { top: 71px; }
  .icon--mail { top: 111px; }
  .icon--web { top: 152px; }

  .brand {
    position: absolute;
    font-weight: 800;
    color: var(--ink);
    letter-spacing: 1px;
    line-height: 1;
    text-align: center;
  }
  .brand--front {
    left: 520px;
    width: 280px;
    top: 232px;
    font-size: 42px;
  }
  .brand--back {
    left: 0;
    width: 876px;
    top: 214px;
    font-size: 86px;
    letter-spacing: 2px;
  }
</style>
</head>
<body>
  <section class="card card--front">
    <div class="contact-panel">
      <div class="person">
        <p class="person__name">CLIENT NAME</p>
        <p class="person__title">Designation</p>
      </div>
      <ul class="contact-list">
        <li>555-555-5555</li>
        <li>5550 142 368</li>
        <li>email@ridgemont.com</li>
        <li>www.ridgemont.com</li>
      </ul>
      <div class="icon-bar">
        <svg class="icon--phone" viewBox="0 0 24 24"><path d="M5 3h4l2 5-3 2a12 12 0 0 0 6 6l2-3 5 2v4a2 2 0 0 1-2 2A17 17 0 0 1 3 5a2 2 0 0 1 2-2z" fill="#fff" stroke="none"/></svg>
        <svg class="icon--mobile" viewBox="0 0 24 24"><rect x="7" y="2" width="10" height="20" rx="2"/><line x1="11" y1="18" x2="13" y2="18"/></svg>
        <svg class="icon--mail" viewBox="0 0 24 24"><rect x="3" y="5" width="18" height="14" fill="#fff" stroke="none"/><path d="M3 5l9 7 9-7" stroke="#0d0d0d"/></svg>
        <svg class="icon--web" viewBox="0 0 24 24"><circle cx="12" cy="12" r="9"/><ellipse cx="12" cy="12" rx="4" ry="9"/><line x1="3" y1="12" x2="21" y2="12"/></svg>
      </div>
    </div>
    <p class="brand brand--front">RIDGEMONT</p>
  </section>

  <section class="card card--back">
    <p class="brand brand--back">RIDGEMONT</p>
  </section>
</body>
</html>
```